Sonstige Verpackung für Sondermaschinenbauer
Zielgruppe
Wir sind ein Sondermaschinenbauer und benötigen ein Design für ein entwickletes Produkt. Das Produkt ist eine Ladestation für Elektroautos.
Aufgabenstellung
Für das Design wünschen wir uns, dass folgende Informationen untergbracht werden:
1. Firmenname (KALVO-MAT)
2. Servicehotlinie
3. Kennzeichnung der RFID-Sensorpunkte (damit der Benutzer der Ladesäule seine Ladekarte an richtiger Stelle vorhält)
Die gezeigten Bilder sind Beispielbilder mit ersten Designversuchen der o.g. Angaben von uns.
Zu sehen auf dem Bild das fertige Produkt Ladesäule, für die wir jetzt noch das finale Design mit den o.g. Angaben benötigen.
Wichtig ist, dass sich die Fläche die designt werden kann, ausschließlich auf die schwarze Kunststoffblende er Säule begrenzt (siehe Bild 1 roter Rahmen). Des weiteren müssen für das Design die blauen LED-Lampen zu berücksichtigt werden, die den Betriebszustand der Ladestation anzeigen (dürfen nicht verdeckt werden).
Firmenlogo ist als Datei angehängt. Müsste aber nicht zwingend so als Block verwendet werden.

```html
<!DOCTYPE html>
<html lang="de">
<head>
<meta charset="utf-8">
<title>KALVO-MAT Ladestation Blende</title>
<link rel="stylesheet" href="https://fonts.googleapis.com/css2?family=Roboto:wght@400;500;700&display=swap">
<style>
  :root {
    --bg: #ece8e2;
    --panel: #0b0b0d;
    --panel-edge: #1c1c20;
    --panel-inner: #111114;
    --text: #ffffff;
    --led: #1f2cff;
    --led-glow: rgba(40, 60, 255, 0.55);
  }
  * { margin: 0; padding: 0; box-sizing: border-box; }
  html, body {
    width: 900px;
    height: 1200px;
    overflow: hidden;
    background: var(--bg);
  }
  .canvas {
    position: relative;
    width: 900px;
    height: 1200px;
  }
  .cover-panel {
    position: absolute;
    left: 40px;
    top: 190px;
    width: 820px;
    height: 820px;
    background: var(--panel);
    border: 10px solid var(--panel-edge);
    border-radius: 22px;
    font-family: "Roboto", sans-serif;
    color: var(--text);
  }
  .panel-field {
    position: absolute;
    inset: 40px;
    background: var(--panel-inner);
    border-radius: 10px;
  }
  .status-led {
    position: absolute;
    top: 252px;
    width: 82px;
    height: 82px;
    border-radius: 50%;
    background: radial-gradient(circle at 40% 40%, #4f5cff 0%, var(--led) 55%, #0f18b0 100%);
    box-shadow: 0 0 26px var(--led-glow);
  }
  .status-led--left { left: 160px; }
  .status-led--right { left: 578px; }
  .hotline {
    position: absolute;
    top: 362px;
    left: 0;
    width: 100%;
    text-align: center;
  }
  .hotline-label {
    font-size: 21px;
    font-weight: 400;
    letter-spacing: 0.5px;
  }
  .hotline-number {
    margin-top: 8px;
    font-size: 46px;
    font-weight: 700;
    letter-spacing: 0.5px;
  }
  .rfid-mark {
    position: absolute;
    top: 520px;
    width: 104px;
    height: 104px;
  }
  .rfid-mark--left { left: 150px; }
  .rfid-mark--right { left: 566px; }
  .brand {
    position: absolute;
    top: 688px;
    left: 0;
    width: 100%;
    display: flex;
    justify-content: center;
    align-items: center;
    gap: 14px;
  }
  .brand-square {
    width: 34px;
    height: 34px;
    border: 4px solid var(--text);
    border-radius: 4px;
  }
  .brand-name {
    font-size: 40px;
    font-weight: 700;
    letter-spacing: 1px;
  }
</style>
</head>
<body>
<div class="canvas">
  <div class="cover-panel">
    <div class="panel-field"></div>

    <span class="status-led status-led--left" aria-label="Status-LED Ladepunkt links"></span>
    <span class="status-led status-led--right" aria-label="Status-LED Ladepunkt rechts"></span>

    <div class="hotline">
      <p class="hotline-label">SERVICEHOTLINIE</p>
      <p class="hotline-number">+49 4321 5588 100</p>
    </div>

    <svg class="rfid-mark rfid-mark--left" viewBox="0 0 100 100" aria-label="RFID-Lesefeld links">
      <rect x="6" y="22" width="64" height="72" rx="6" fill="none" stroke="#fff" stroke-width="5"/>
      <rect x="2" y="66" width="72" height="22" fill="#111114"/>
      <text x="38" y="84" text-anchor="middle" font-family="Roboto, sans-serif" font-weight="700" font-size="19" fill="#fff">RFID</text>
      <circle cx="62" cy="38" r="5" fill="#fff"/>
      <path d="M62 22 A16 16 0 0 1 78 38" fill="none" stroke="#fff" stroke-width="5"/>
      <path d="M62 12 A26 26 0 0 1 88 38" fill="none" stroke="#fff" stroke-width="5"/>
      <path d="M62 2 A36 36 0 0 1 98 38" fill="none" stroke="#fff" stroke-width="5"/>
    </svg>

    <svg class="rfid-mark rfid-mark--right" viewBox="0 0 100 100" aria-label="RFID-Lesefeld rechts">
      <rect x="6" y="22" width="64" height="72" rx="6" fill="none" stroke="#fff" stroke-width="5"/>
      <rect x="2" y="66" width="72" height="22" fill="#111114"/>
      <text x="38" y="84" text-anchor="middle" font-family="Roboto, sans-serif" font-weight="700" font-size="19" fill="#fff">RFID</text>
      <circle cx="62" cy="38" r="5" fill="#fff"/>
      <path d="M62 22 A16 16 0 0 1 78 38" fill="none" stroke="#fff" stroke-width="5"/>
      <path d="M62 12 A26 26 0 0 1 88 38" fill="none" stroke="#fff" stroke-width="5"/>
      <path d="M62 2 A36 36 0 0 1 98 38" fill="none" stroke="#fff" stroke-width="5"/>
    </svg>

    <div class="brand">
      <span class="brand-square"></span>
      <span class="brand-name">KALVO-MAT</span>
    </div>
  </div>
</div>
</body>
</html>
```